Restaurant business revamping our look and need a new modern menu

We need a new menu that is appealing, similar to the look of our new logo while also keeping our "cozy, clean, Midland staple" feel and gets peoples eyes on the high price items and top sellers. We are a deli that's been around since 1984, with lots of Burgers, Curly Fries, Reuben, Salads, etc.
Once we like that menu, we will need our pizza specials menu updated to look similar.

Please refer to our website for menu word format www.haldensofbrookvale.com

Target Market(s)

Every day Midlanders

Industry/Entity Type

Restaurant

Requirements
Must have
• Current menu is a trifold - not a must have but nice layout

```html
<!DOCTYPE html>
<html lang="en">
<head>
<meta charset="utf-8">
<title>Halden's Menu</title>
<link href="https://fonts.googleapis.com/css2?family=Playfair+Display+SC:wght@700&family=Oswald:wght@500&family=Lora:ital,wght@0,400;1,400&display=swap" rel="stylesheet">
<style>
:root{
  --paper:#f1f0ee;
  --ink:#3a3a3a;
  --panel:#3e3e40;
  --panel-ink:#f2f2f2;
  --muted:#5a5a5a;
}
*{margin:0;padding:0;box-sizing:border-box}
html,body{width:1200px;height:849px;overflow:hidden;background:var(--paper)}
.menu{position:relative;width:1200px;height:849px;background:var(--paper);color:var(--ink);font-family:"Oswald",sans-serif}
.title{position:absolute;font-family:"Playfair Display SC",serif;font-weight:700;font-size:38px;letter-spacing:-.01em;line-height:1;color:var(--ink);white-space:nowrap}
.title--compact{font-size:33px}
.item{position:absolute;display:flex;justify-content:space-between;align-items:center;font-size:15px;font-variant:small-caps;letter-spacing:.05em;line-height:18px;height:18px;white-space:nowrap}
.note{position:absolute;font-family:"Lora",serif;font-style:italic;font-size:10px;color:var(--muted);line-height:12px;white-space:nowrap}
.frame{position:absolute;background:var(--ink)}
.pick{display:inline-block;width:11px;height:11px;border-radius:50%;background:var(--ink);border:2px solid var(--paper);box-shadow:0 0 0 1px var(--ink);vertical-align:middle;margin:0 5px}
.beer .pick{background:var(--panel-ink);border-color:var(--panel);box-shadow:0 0 0 1px var(--panel-ink)}
.legend{position:absolute;left:0;width:1212px;top:9px;font-family:"Lora",serif;font-size:13px;text-align:center}
.soup-line{position:absolute;left:24px;width:352px;text-align:center;font-size:13px;font-variant:small-caps;letter-spacing:.05em;line-height:15px;white-space:nowrap}
.size{font-family:"Lora",serif;font-style:italic;font-variant:normal;letter-spacing:0;color:var(--muted);font-size:11px}
.size b{font-family:"Oswald",sans-serif;font-style:normal;font-weight:500;color:var(--ink);margin-right:30px}
.beer{position:absolute;left:408px;top:193px;width:383px;height:373px;background:var(--panel);color:var(--panel-ink)}
.beer .title{color:var(--panel-ink)}
.beer .note{color:#d6d6d6}
.beer-desc{position:absolute;left:18px;top:128px;width:345px;font-family:"Lora",serif;font-style:italic;font-size:9.5px;line-height:14px;color:#d6d6d6}
.wine-col{position:absolute;font-size:13px;letter-spacing:.04em}
.photo{position:absolute}
.address{position:absolute;left:413px;width:386px;top:757px;text-align:center;font-family:"Lora",serif;font-style:italic;font-size:14px;line-height:18px}
.contact{position:absolute;top:802px;display:flex;align-items:center;gap:8px;font-size:13px}
.dot{width:17px;height:17px;border-radius:50%;background:var(--ink)}
.brand{position:absolute;left:858px;top:427px;width:180px;height:180px;border-radius:50%;border:2px solid var(--ink);background:rgba(241,240,238,.88);display:flex;align-items:center;justify-content:center;font-family:"Playfair Display SC",serif;font-weight:700;font-size:34px;color:#1d1d1d}
.philosophy{position:absolute;left:822px;width:350px;top:661px;text-align:center;font-family:"Lora",serif;font-style:italic;font-size:11.6px;line-height:15px}
.philosophy strong{font-family:"Oswald",sans-serif;font-style:normal;font-size:14px;letter-spacing:.05em}
</style>
</head>
<body>
<main class="menu">

  <p class="legend"><span class="pick"></span>- must try/recommended/Proprietor's choice</p>

  <section class="soup">
    <div class="frame" style="left:200px;top:34px;width:180px;height:3px"></div>
    <div class="frame" style="left:377px;top:34px;width:3px;height:170px"></div>
    <div class="frame" style="left:21px;top:176px;width:205px;height:3px"></div>
    <div class="frame" style="left:22px;top:47px;width:3px;height:131px"></div>
    <h2 class="title" style="left:29px;top:33px">Soup</h2>
    <p class="soup-line" style="top:75px">Cream of Broccoli, Potato with Bacon, Wisconsin Cheese</p>
    <p class="soup-line" style="top:88px">Tomato Basil, Chicken Noodle</p>
    <p class="soup-line" style="top:104px"><span class="size">Cup <b>4.25</b>Bowl <b style="margin:0">5.25</b></span></p>
    <p class="soup-line" style="top:128px">Seafood Gumbo</p>
    <p class="soup-line" style="top:147px"><span class="size">Cup <b>5.50</b>Bowl <b style="margin:0">6.50</b></span></p>
  </section>

  <section class="appetizer">
    <h2 class="title" style="right:839px;top:192px">Appetizer</h2>
    <p class="item" style="left:38px;width:324px;top:234px"><span>Breaded Cheese Sticks <span class="pick"></span></span><span>10.50</span></p>
    <p class="note" style="left:38px;top:253px">homemade marinara</p>
    <p class="item" style="left:38px;width:324px;top:248px;justify-content:flex-end"><span>+ 1.25</span></p>
    <p class="item" style="left:38px;width:324px;top:269px"><span>Zucchini Chips</span><span>9.95</span></p>
    <p class="item" style="left:38px;width:324px;top:292px"><span>Onion Rings</span><span>9.95</span></p>
    <p class="item" style="left:38px;width:324px;top:316px"><span>Chips &amp; Queso</span><span>6.25</span></p>
    <p class="item" style="left:38px;width:324px;top:339px"><span>Potachos</span><span>10.05</span></p>
    <p class="item" style="left:38px;width:324px;top:362px"><span>Blackened or Grilled Chicken</span><span>12.25</span></p>
  </section>

  <section class="kids">
    <div class="frame" style="left:128px;top:396px;width:252px;height:3px"></div>
    <div class="frame" style="left:377px;top:396px;width:3px;height:147px"></div>
    <div class="frame" style="left:128px;top:540px;width:252px;height:3px"></div>
    <div class="frame" style="left:22px;top:423px;width:30px;height:3px"></div>
    <div class="frame" style="left:22px;top:423px;width:3px;height:210px"></div>
    <h2 class="title" style="left:52px;top:396px">Kids</h2>
    <p class="soup-line" style="left:180px;width:186px;top:407px">Mac and Cheese</p>
    <p class="soup-line" style="left:180px;width:186px;top:423px"><span class="size">Cup <b>3.00</b>Bowl <b style="margin:0">4.50</b></span></p>
    <p class="item" style="left:37px;width:325px;top:441px"><span>6.00</span><span>Peanut Butter &amp; Jelly With Side</span></p>
    <p class="item" style="left:37px;width:325px;top:465px"><span>6.25</span><span>Grilled Cheese Sandwich With Side</span></p>
    <p class="item" style="left:37px;width:325px;top:489px"><span>6.25</span><span>All Beef Hotdog</span></p>
    <p class="item" style="left:37px;width:325px;top:512px"><span>1.50</span><span>Apple Juice</span></p>
  </section>

  <section class="desserts">
    <h2 class="title" style="right:820px;top:552px">Desserts</h2>
    <p class="item" style="left:38px;width:324px;top:592px"><span>Iced Brownies</span><span>2.15</span></p>
    <p class="item" style="left:38px;width:324px;top:615px"><span>Carrot Cake</span><span>4.00</span></p>
    <p class="item" style="left:38px;width:324px;top:638px"><span>Boston Cream Pie</span><span>4.00</span></p>
    <p class="item" style="left:38px;width:324px;top:661px"><span>Newyork Colossal Cheesecake</span><span>6.25</span></p>
    <p class="item" style="left:38px;width:324px;top:684px"><span>Key Lime Pie</span><span>6.25</span></p>
    <p class="item" style="left:38px;width:324px;top:707px"><span>Chocolate Mouse Cake</span><span>6.50</span></p>
    <p class="item" style="left:38px;width:324px;top:730px"><span>The "Real Deal" Cannoli</span><span>6.50</span></p>
    <p class="item" style="left:38px;width:324px;top:754px"><span>Lemon Tart</span><span>3.25</span></p>
    <p class="item" style="left:38px;width:324px;top:781px"><span>Texas Chocolate Sheet Cake</span><span>4.50</span></p>
    <p class="item" style="left:38px;width:324px;top:805px"><span>Italian Cream Cake</span><span>4.50</span></p>
  </section>

  <section class="drinks">
    <h2 class="title title--compact" style="left:409px;top:38px">Drinks</h2>
    <p class="item" style="left:558px;width:215px;top:35px"><span>Large Drinks</span><span>3.39</span></p>
    <p class="item" style="left:558px;width:215px;top:56px"><span>Clear Spring Water</span><span>3.45</span></p>
    <p class="item" style="left:428px;width:345px;top:77px"><span>Fizz Cola, Diet Fizz, Cherry Fizz, Lime Spark, Root Beer,</span></p>
    <p class="item" style="left:428px;width:345px;top:92px"><span>Dr. Bramble, Tea, Taspberry Tea, Lemonade, Rio</span></p>
    <p class="item" style="left:428px;width:345px;top:108px"><span>Claro</span><span>2.49</span></p>
    <p class="item" style="left:426px;width:347px;top:132px"><span>Coffee (Regular or Decaf)</span><span>2.49</span></p>
    <p class="note" style="left:426px;top:148px">we proudly brew Crema Pod</p>
    <p class="item" style="left:426px;width:347px;top:163px"><span>Bottled Water</span><span>1.95</span></p>
  </section>

  <section class="beer">
    <h2 class="title" style="left:19px;top:11px">Beer</h2>
    <p class="item" style="left:150px;width:215px;top:14px"><span>Domestic on Tap</span><span>4.50</span></p>
    <p class="note" style="left:150px;top:31px;font-size:11px">Ridge Light</p>
    <p class="item" style="left:18px;width:347px;top:50px"><span>Bottled Water</span></p>
    <p class="note" style="left:18px;top:67px;font-style:normal;font-size:11px">Domestic</p>
    <p class="note" style="left:18px;top:79px;font-style:normal;font-size:11px">Specialty</p>
    <p class="note" style="right:18px;top:67px;font-style:normal;font-size:10px">4.25</p>
    <p class="note" style="right:18px;top:79px;font-style:normal;font-size:10px">4.95</p>
    <p class="item" style="left:18px;width:347px;top:98px"><span>Specialty &amp; Microbrew</span><span>3.39</span></p>
    <p class="item" style="left:18px;width:347px;top:112px"><span>Draft Beer</span></p>
    <p class="beer-desc">Half &amp; Half <span class="pick"></span> (Redhand Ale topped with Blackmoor Stout), Tall Mesa Brewing Co. - Six Steps (American Amber) (Midland, Texas), Tall Mesa Brewing Co. - Hazy Daze (IPA) (Midland,TX), Oddfellow Brewing Co. - Rotating Beer (Midland, TX), Blackmoor Stout, Dos Lunas, Redhand Ale, Belle Etoile, Prairie Bock</p>

    <h2 class="title" style="right:18px;top:198px">&amp; Wines</h2>
    <p class="wine-col" style="left:18px;top:209px;font-family:'Lora',serif">Bottle</p>
    <p class="note" style="left:18px;top:224px;color:#d6d6d6">(375ml.)</p>
    <p class="wine-col" style="left:115px;top:209px;font-family:'Lora',serif">Glass</p>

    <p class="item" style="left:18px;width:347px;top:241px"><span>19.00</span><span style="flex:1;margin-left:58px">10.00</span><span><span class="pick"></span>Canyon Ridge Chardonnay</span></p>
    <p class="item" style="left:18px;width:347px;top:262px"><span>16.00</span><span style="flex:1;margin-left:58px">8.75</span><span><span class="pick"></span>Bramwell Valley Cab</span></p>
    <p class="item" style="left:18px;width:347px;top:283px"><span>14.00</span><span style="flex:1;margin-left:58px">7.75</span><span><span class="pick"></span>Vista Clara Pinot Noir</span></p>
    <p class="item" style="left:18px;width:347px;top:304px"><span>13.00</span><span style="flex:1;margin-left:58px">7.50</span><span><span class="pick"></span>Route 12 Sauvignon Blanc</span></p>
    <p class="item" style="left:115px;width:250px;top:325px"><span>7.50</span><span><span class="pick"></span>White Zinfandel</span></p>
    <p class="item" style="left:115px;width:250px;top:345px"><span>7.50</span><span>Pinot Grigio</span></p>
  </section>

  <svg class="photo" style="left:410px;top:585px" width="382" height="160" viewBox="0 0 382 160" role="img" aria-label="Photo of a blackened chicken spinach salad with red onion">
    <defs>
      <linearGradient id="saladTone" x1="0" y1="0" x2="1" y2="1">
        <stop offset="0" stop-color="#8a5a2c"/>
        <stop offset=".45" stop-color="#3f6a2a"/>
        <stop offset="1" stop-color="#2c4a1e"/>
      </linearGradient>
    </defs>
    <polygon points="14,12 372,6 366,70 380,150 20,156 2,110 10,60" fill="url(#saladTone)"/>
  </svg>

  <svg class="photo" style="left:790px;top:0" width="410" height="570" viewBox="0 0 410 570" role="img" aria-label="Photo of a scoop of chicken salad dusted with paprika on greens">
    <defs>
      <radialGradient id="chickenTone" cx=".6" cy=".45" r=".7">
        <stop offset="0" stop-color="#d9d1c7"/>
        <stop offset=".5" stop-color="#c2b3a3"/>
        <stop offset=".85" stop-color="#5c7a38"/>
        <stop offset="1" stop-color="#3d5a26"/>
      </radialGradient>
    </defs>
    <polygon points="318,0 410,0 410,565 40,565 10,430 60,250 200,110" fill="url(#chickenTone)"/>
  </svg>

  <div class="brand">Halden's</div>

  <p class="address">1480 W. Alder Midland, Texas 79700<br>555.014.2290</p>
  <p class="contact" style="left:414px"><span class="dot"></span>www.haldensonbrookvale.com</p>
  <p class="contact" style="left:671px"><span class="dot"></span>@haldens_deli</p>

  <p class="philosophy">Only the finest ingredients, the choicest cuts of meats and the freshest produce will be good enough for our customers. Our beef products are from the round cut (leanest possible) therefore the most "heart healthy". Our turkey is smoked breast 98% fat free. We make our salads fresh from scratch. We want you to know these facts so you will understand why we feel we are unique in the Permian Basin. To state our philosophy in a single word, it is <strong>"QUALITY"</strong>.</p>

</main>
</body>
</html>
```